Hiring Infographic

We need an infographic for displaying on a website and sharing via social media. Attached is an example of a prior infographic developed for the client for reference (Orchard Ledger). The data for the new infographic is in the attached Mocrosoft Word document about hiring.

Media

```html
<!DOCTYPE html>
<html lang="en">
<head>
<meta charset="utf-8">
<title>Hiring the Right People – Why Potential Trumps Everything Else</title>
<link rel="stylesheet" href="https://fonts.googleapis.com/css2?family=Oswald:wght@400;500;600&family=Open+Sans:wght@400;600;700&display=swap">
<style>
:root{
  --navy:#1f3b5c;
  --header:#2c3e52;
  --band:#4b5058;
  --ink:#3a3f45;
  --muted:#5c636b;
  --paper:#ffffff;
  --rule:#d7dbe0;
  --red:#e2433b;
  --orange:#f39a32;
  --blue:#2b7bbb;
  --green:#8cbf3f;
  --flame:#e4472c;
}
*{box-sizing:border-box;margin:0;padding:0}
html,body{width:1200px;height:3478px;overflow:hidden;background:var(--paper)}
body{font-family:"Open Sans",Arial,sans-serif;color:var(--ink);font-size:15px;line-height:1.4}
.page{position:relative;width:1200px;height:3478px}
section{overflow:hidden}

.title-bar{height:64px;background:var(--header);color:#fff;font-family:"Oswald",Arial,sans-serif;font-weight:500;font-size:30px;letter-spacing:1px;display:flex;align-items:center;justify-content:center;text-transform:uppercase}
.intro{height:250px;padding:28px 60px 0;text-align:center}
.intro p{margin-bottom:18px}

.band{height:50px;margin:0 160px;background:var(--band);color:#fff;font-family:"Oswald",Arial,sans-serif;font-weight:500;font-size:28px;letter-spacing:1px;display:flex;align-items:center;justify-content:center;text-transform:uppercase}

.forces{height:470px;display:flex;justify-content:space-between;padding:34px 70px 0}
.force{width:320px;text-align:center}
.force-icon{width:150px;height:150px;border-radius:50%;background:var(--navy);margin:0 auto 18px;display:flex;align-items:center;justify-content:center}
.force h3{font-family:"Oswald",Arial,sans-serif;font-weight:600;font-size:30px;color:var(--navy);letter-spacing:1px;margin-bottom:8px;line-height:1.2}
.force p{font-size:15px;line-height:1.4}

.qualities{height:610px;padding:40px 60px 0}
.quality-row{display:flex;justify-content:space-between;margin-bottom:50px}
.quality-row.second{justify-content:center;gap:80px}
.quality{width:340px;display:flex;gap:18px;align-items:flex-start}
.quality-icon{flex:0 0 140px;height:140px;border-radius:50%;display:flex;align-items:center;justify-content:center}
.quality h3{font-family:"Oswald",Arial,sans-serif;font-weight:600;font-size:26px;letter-spacing:1px;margin:2px 0 6px;text-transform:uppercase;line-height:1.2}
.quality p{font-size:15px;line-height:1.4}
.motivation .quality-icon{background:var(--red)}.motivation h3{color:var(--red)}
.curiosity .quality-icon{background:var(--orange)}.curiosity h3{color:var(--orange)}
.insight .quality-icon{background:var(--blue)}.insight h3{color:var(--blue)}
.engagement .quality-icon{background:var(--green)}.engagement h3{color:var(--green)}
.determination .quality-icon{background:var(--flame)}.determination h3{color:var(--flame)}

.panel{display:flex;margin:0 48px 22px;border-top:3px solid var(--rule)}
.panel-label{flex:0 0 360px;align-self:center;background:var(--navy);color:#fff;font-family:"Oswald",Arial,sans-serif;font-weight:500;font-size:38px;line-height:1.12;text-transform:uppercase;padding:18px 54px 18px 26px;clip-path:polygon(0 0,90% 0,100% 50%,90% 100%,0 100%)}
.panel-body{flex:1;padding:20px 0 0 34px}
.panel-body p{margin-bottom:10px}
.panel-body ul{padding-left:22px}
.panel-body li{margin-bottom:4px}
.panel-body ul ul{list-style:"– ";margin-top:3px}
.panel-body ul ul li{margin-bottom:1px}
.panel-body ol{padding-left:26px;margin-top:4px}
.panel-body ol li{margin-bottom:1px}
.panel-body strong{color:var(--navy)}
.evaluate{height:320px;margin-top:30px}
.retain{height:340px}
.else{height:450px}
.cost{height:450px}
.cost h4{font-weight:700;color:var(--navy);font-size:16px;margin-bottom:4px}

.connect{height:250px;margin:0 48px;border-top:3px solid var(--rule);display:flex;align-items:center;justify-content:space-between;gap:40px}
.connect h2{font-family:"Oswald",Arial,sans-serif;font-weight:600;font-size:34px;color:var(--navy);text-transform:uppercase;line-height:1.15;margin-bottom:10px}
.connect p{font-size:16px;line-height:1.45}
.brand{display:flex;align-items:center;gap:16px;font-family:"Oswald",Arial,sans-serif;font-weight:500;font-size:44px;color:var(--navy);line-height:1;white-space:nowrap}
.brand-dot{width:30px;height:30px;border-radius:50%;background:var(--navy)}

.source{position:absolute;left:48px;bottom:24px;font-size:14px;color:var(--muted)}
</style>
</head>
<body>
<div class="page">

  <header class="title-bar">Hiring the Right People – Why Potential Trumps Everything Else</header>

  <section class="intro">
    <p>According to global leadership expert Tomas Valdivieso-Reyes, potential tops brains, experience and competencies when evaluating employees. It's the number one predictor of success at all levels in every size organization.</p>
    <p>The hallmarks of potential include the ability to adapt and grow. Because companies operate in an increasingly volatile and complex world, they need employees who can easily acclimate to an ever-changing business environment and grow into challenging new roles. Employees must be able to succeed today and tomorrow, regardless of how much things change.</p>
    <p>That's why you can't use a competency-only based evaluation criteria when hiring. It's just impossible to predict the qualifications needed to succeed down the road. Hiring right means identifying candidates with the greatest potential and helping them flourish once they're on your team.</p>
  </section>

  <h2 class="band">Three Forces Contributing to Senior Talent Scarcity</h2>

  <section class="forces">
    <div class="force">
      <div class="force-icon">
        <svg width="92" height="92" viewBox="0 0 92 92" fill="none" stroke="#fff" stroke-width="5"><circle cx="46" cy="46" r="40"/><ellipse cx="46" cy="46" rx="17" ry="40"/><line x1="6" y1="46" x2="86" y2="46"/><path d="M12 26h68M12 66h68"/></svg>
      </div>
      <h3>GLOBALIZATION</h3>
      <p>With the pace of globalization charging full steam ahead, companies in developed and developing nations must compete for talent like never before. For example, the Global Economic Council predicts 70% of the world's growth by 2016 will come from emerging markets.</p>
    </div>
    <div class="force">
      <div class="force-icon">
        <svg width="96" height="80" viewBox="0 0 96 80" fill="#fff"><circle cx="48" cy="20" r="14"/><path d="M24 76c0-18 10-30 24-30s24 12 24 30z"/><circle cx="18" cy="30" r="10"/><path d="M0 76c0-14 7-24 18-24 5 0 9 2 12 5-4 5-6 12-6 19z"/><circle cx="78" cy="30" r="10"/><path d="M96 76c0-14-7-24-18-24-5 0-9 2-12 5 4 5 6 12 6 19z"/></svg>
      </div>
      <h3>DEMOGRAPHICS</h3>
      <p>The percentage of senior executives in the sought-after 35-to-44-year-old age group has been dwindling. During the past decade, this demographic shift primarily affected the U.S. and Europe. However, by 2020, Russia, Canada, South Korea and China will have more workers entering retirement than the workforce.</p>
    </div>
    <div class="force">
      <div class="force-icon">
        <svg width="96" height="70" viewBox="0 0 96 70" fill="#fff"><rect x="0" y="10" width="14" height="34" rx="2"/><rect x="14" y="18" width="40" height="18"/><rect x="54" y="10" width="12" height="34" rx="2"/><rect x="66" y="18" width="18" height="46"/><rect x="60" y="56" width="30" height="12" rx="2"/></svg>
      </div>
      <h3>PIPELINES</h3>
      <p>Companies remain unsure where they will find the next generation of leaders. According to a Hartwell Advisory 2014 survey of CEOs in 68 countries, 63% of respondents said they were concerned about the future availability of key skills at all levels. In a Calder Strategy Group study, 56% of executives expect critical gaps in their ability to fill senior managerial roles in coming years.</p>
    </div>
  </section>

  <h2 class="band">Identifying Employee Potential – The Five Critical Qualities</h2>

  <section class="qualities">
    <div class="quality-row">
      <div class="quality motivation">
        <div class="quality-icon"><svg width="76" height="68" viewBox="0 0 80 72" fill="#fff"><path d="M40 70 6 36C-4 26 0 6 18 4c10-1 17 5 22 12 5-7 12-13 22-12 18 2 22 22 12 32z"/></svg></div>
        <div><h3>Motivation</h3><p>A powerful commitment to pursue unselfish goals. Highly ambitious with a strong desire to excel. Seeks big, collective goals and shows profound personal humility.</p></div>
      </div>
      <div class="quality curiosity">
        <div class="quality-icon"><svg width="76" height="76" viewBox="0 0 80 80" fill="none" stroke="#fff" stroke-width="8" stroke-linecap="round"><circle cx="32" cy="32" r="22"/><line x1="49" y1="49" x2="72" y2="72"/></svg></div>
        <div><h3>Curiosity</h3><p>Pursues new experiences, knowledge and candid feedback. Remains open to learning and change.</p></div>
      </div>
      <div class="quality insight">
        <div class="quality-icon"><svg width="60" height="80" viewBox="0 0 64 86" fill="#fff"><path d="M32 2C15 2 2 15 2 31c0 11 6 19 13 25v10h34V56c7-6 13-14 13-25C62 15 49 2 32 2z"/><rect x="17" y="70" width="30" height="6" rx="2"/><rect x="21" y="79" width="22" height="6" rx="3"/></svg></div>
        <div><h3>Insight</h3><p>Gathers and makes sense of information that might lead to new possibilities. Sees connections where others don't.</p></div>
      </div>
    </div>
    <div class="quality-row second">
      <div class="quality engagement">
        <div class="quality-icon"><svg width="86" height="66" viewBox="0 0 90 70" fill="none" stroke="#fff" stroke-width="7" stroke-linecap="round" stroke-linejoin="round"><path d="M4 24 22 10l14 6 14-6 36 22M4 24l30 30c4 4 9 4 12 0l22-20"/><path d="M30 40l10 10M38 32l12 12"/></svg></div>
        <div><h3>Engagement</h3><p>Uses emotion and logic to communicate a persuasive vision. Connects with work and people.</p></div>
      </div>
      <div class="quality determination">
        <div class="quality-icon"><svg width="80" height="80" viewBox="0 0 84 84" fill="none" stroke="#fff" stroke-width="7"><circle cx="42" cy="42" r="36"/><circle cx="42" cy="42" r="22"/><circle cx="42" cy="42" r="7" fill="#fff"/></svg></div>
        <div><h3>Determination</h3><p>Fights for difficult goals despite challenges and bounces back from adversity.</p></div>
      </div>
    </div>
  </section>

  <section class="panel evaluate">
    <h2 class="panel-label">How to<br>Evaluate<br>Potential</h2>
    <div class="panel-body">
      <p>To determine if a candidate believes in self-improvement, enjoys learning and can recover from missteps, you need to uncover concrete examples by:</p>
      <ul>
        <li><strong>Digging into personal and professional histories</strong></li>
        <li><strong>Conducting in-depth interviews</strong></li>
        <li><strong>Thoroughly checking references</strong></li>
        <li><strong>Asking pointed questions, such as:</strong>
          <ul>
            <li>How do you react when someone challenges you?</li>
            <li>How do you invite input from others on your team?</li>
            <li>What do you do to broaden your thinking, experience or personal development?</li>
            <li>How do you foster learning in your organization?</li>
            <li>What steps do you take to seek out the unknown?</li>
          </ul>
        </li>
      </ul>
    </div>
  </section>

  <section class="panel retain">
    <h2 class="panel-label">How to Retain<br>High-Potential<br>Talent</h2>
    <div class="panel-body">
      <ul>
        <li>Offer development opportunities that push employees out of their comfort zones, but don't stretch them beyond their limits.</li>
        <li>Create autonomy in the four "T" dimensions:
          <ul>
            <li>Task (what they do)</li>
            <li>Time (when they do it)</li>
            <li>Team (whom they do it with)</li>
            <li>Technique (how they do it)</li>
          </ul>
        </li>
        <li>Design an environment in which employees can master their skills and excel. Help them by setting difficult, yet attainable, challenges and eliminating distractions.</li>
        <li>Establish a purpose in all work so employees know they're serving something bigger than themselves. Engage them in a greater team, organizational or societal goal.</li>
        <li>Compensate high-potential employees to reflect their contribution and effort.</li>
      </ul>
    </div>
  </section>

  <section class="panel else">
    <h2 class="panel-label">What Else<br>Do You<br>Look For?</h2>
    <div class="panel-body">
      <p>Potential is the defining measurement of executives today. However, you should still integrate other evaluation criteria into the hiring decision:</p>
      <ul>
        <li><strong>INTELLIGENCE</strong> – Assess a candidate's general intelligence, including analytical, verbal, mathematical and logical reasoning, by considering educational background, job experience and interview responses.</li>
        <li><strong>VALUES</strong> – Use interviews and reference checks to gauge honesty, integrity and whether the candidate shares your organization's core values.</li>
        <li><strong>LEADERSHIP ABILITIES</strong> – Although position and organization requirements will vary, the best leaders tend to have some measure of these eight abilities:
          <ol>
            <li>Strategic Orientation – Engaging in complex analytical and conceptual thinking</li>
            <li>Market Insight – Understanding the market and how it affects the business</li>
            <li>Results Orientation – Committing to improve key business metrics</li>
            <li>Customer Impact – Passionately serving the customers</li>
            <li>Collaboration and Influence – Working with peers or partners not in the chain of command</li>
            <li>Organizational Development – Attracting and developing top talent</li>
            <li>Team Leadership – Building valuable groups</li>
            <li>Change Leadership – Transforming and aligning an organization around a new goal</li>
          </ol>
        </li>
      </ul>
    </div>
  </section>

  <section class="panel cost">
    <h2 class="panel-label">The Cost<br>of a Bad<br>Hire</h2>
    <div class="panel-body">
      <p>When you make a bad hiring decision, the cost to the organization can be staggering. Not only will the business lose the money it sunk into sourcing, recruiting and hiring, but the loss in productivity will ripple throughout the company.</p>
      <h4>Some eye-opening stats include:</h4>
      <ul>
        <li>The National Labor Studies Office determined the average cost of a bad hiring decision can equal 30% of the employee's first-year salary.</li>
        <li>According to TalentDesk, it costs $7,000 to replace one salaried employee, $10,000 to replace a mid-level employee, and $40,000 to replace a senior executive.</li>
        <li>A Northbridge Management Review study found as much as 80% of employee turnover can be attributed to bad hiring decisions.</li>
        <li>In a 2012 Civic Business Research Institute survey, 66% of employers said they experienced negative effects of bad hires, with 37% of that number affecting employee morale, 18% impacting client relationships and 10% causing a decrease in sales.</li>
      </ul>
      <p>Serving Arizona businesses since 1994, Meridian Staffing Group offers a full spectrum of workforce solutions, including talent sourcing, temp staffing, recruitment and assessment consulting and coaching, matching the highest caliber candidates to fit specific corporate cultures, with a 94% retention rate of placed candidates.</p>
    </div>
  </section>

  <section class="connect">
    <div>
      <h2>Connect with Meridian<br>Staffing Group Today</h2>
      <p>Phone: 555-014-2290<br>Web: www.MeridianStaffing.example<br>Twitter: @meridianjobs<br>Facebook: facebook.com/meridianstaffing</p>
    </div>
    <div class="brand"><span class="brand-dot"></span>Meridian Staffing Group</div>
  </section>

  <p class="source">Source: "Choosing the Who: Building Teams Around Potential," Tomas Valdivieso-Reyes</p>
</div>
</body>
</html>
```